ReDesign Website for a more Bold approach

Hello! I'd like to redesign my website: holvencrest.com

I'd like to add one thing that's not on my website which is a blog. The design around the blog should be put time into as I will be putting out incredibly great content and want it to attract viewers.

I get a lot of inspiration from ruvtal.com (the way they flow the big statements across each screen, colors)
moorlane.vc (the simplicity behind the design is beautiful)

I like modern very simple but bold approaches.

I am going to attach my logo here and if it can be thought of when making the design of the website. Thanks!

Industry/Entity Type

Finance and Private Equity

Number of Pages Required

3 page

Font styles to use
Serif
Sans Serif

Colors
0054AA
0677BA
7BADD7
CADEEF
E8F1F8
0094D4
00A9DD
6FCCEA
C7EBF8
E9F6FB
00AB8E
00BBA5
67D7C9
C6EFE9
E9F9F6

Requirements
Must have
• My project must have a Home, Expertise, Story, Clients, Approach, Blog, Contact
Nice to have
• It would be nice to have these tabs reduced to 1-3 pages
Should not have
• My project must not have bright colors.

```html
<!DOCTYPE html>
<html lang="en">
<head>
<meta charset="UTF-8">
<title>Contact – Holvencrest</title>
<link rel="stylesheet" href="https://fonts.googleapis.com/css2?family=Alike&family=Poppins:wght@400;500;600&display=swap">
<style>
  :root {
    --navy: #0b2845;
    --hero-start: #0a2a4c;
    --hero-mid: #0f3a66;
    --hero-end: #1d4f6e;
    --blue: #0054aa;
    --blue-mid: #0677ba;
    --sky: #6fccea;
    --teal: #00ab8e;
    --teal-soft: #c6eff0;
    --mist: #e8f1f8;
    --white: #ffffff;
    --ink: #101820;
    --body-gray: #555a60;
    --field-text: #6b6f75;
  }
  * { box-sizing: border-box; margin: 0; padding: 0; }
  html, body { width: 691px; height: 1200px; overflow: hidden; background: var(--white); }
  body { position: relative; font-family: "Poppins", sans-serif; color: var(--ink); }

  .hero {
    position: absolute; left: 0; top: 0; width: 691px; height: 255px;
    background: linear-gradient(100deg, var(--hero-start) 0%, var(--hero-mid) 50%, var(--hero-end) 100%);
  }
  .brand { position: absolute; font-weight: 600; color: var(--white); font-size: 11px; letter-spacing: 1.4px; line-height: 1; white-space: nowrap; }
  .site-nav a { position: absolute; top: 40px; font-size: 8.2px; font-weight: 500; color: var(--white); text-decoration: none; white-space: nowrap; line-height: 1; }
  .site-nav a.current { color: var(--sky); }

  .hero-title { position: absolute; left: 66px; top: 96px; font-family: "Alike", serif; font-size: 53px; font-weight: 400; color: var(--white); line-height: 1; letter-spacing: 1.5px; white-space: nowrap; }
  .hero-lead { position: absolute; left: 71px; top: 160px; font-size: 7.2px; line-height: 15px; color: var(--white); white-space: nowrap; }

  .section-title { position: absolute; left: 0; width: 691px; top: 354px; text-align: center; font-family: "Alike", serif; font-size: 42px; line-height: 1; color: var(--ink); letter-spacing: 1.5px; }
  .section-lead { position: absolute; left: 0; width: 691px; top: 410px; text-align: center; font-size: 7.2px; line-height: 15px; color: var(--body-gray); white-space: nowrap; }

  .field { position: absolute; border: 1px solid var(--blue-mid); border-radius: 5px; background: var(--white); font-size: 8.8px; color: var(--field-text); padding-left: 14px; }
  .field.line { width: 197px; height: 30px; line-height: 28px; left: 126px; }
  .field.message { left: 342px; top: 468px; width: 227px; height: 115px; padding-top: 7px; }
  .submit { position: absolute; left: 272px; top: 606px; width: 147px; height: 27px; border-radius: 4px; background: var(--blue-mid); color: var(--white); font-size: 9.5px; font-weight: 500; text-align: center; line-height: 27px; }

  .map { position: absolute; left: 0; top: 726px; width: 691px; height: 226px; background: linear-gradient(90deg, var(--mist) 0%, var(--teal-soft) 40%, var(--mist) 70%, #e9f6fb 100%); border-bottom: 1px solid var(--blue-mid); }
  .map-pin { position: absolute; left: 323px; top: 795px; }

  .footer { position: absolute; left: 0; top: 952px; width: 691px; height: 248px; background: var(--navy); color: var(--white); }
  .footer-about { position: absolute; left: 80px; top: 104px; font-size: 7.2px; line-height: 12px; white-space: nowrap; }
  .copyright { position: absolute; left: 80px; top: 152px; font-size: 7.2px; }
  .copyright span { color: var(--sky); }
  .footer-heading { position: absolute; top: 68px; font-family: "Alike", serif; font-size: 15px; font-weight: 400; line-height: 1; }
  .footer-links a { position: absolute; left: 289px; font-size: 7.2px; font-weight: 500; color: var(--white); text-decoration: none; line-height: 1; }
  .footer-links a.current { color: var(--sky); }
  .address { position: absolute; left: 402px; top: 109px; font-size: 13.5px; font-weight: 600; white-space: nowrap; }
  .phone-row { position: absolute; left: 401px; top: 135px; display: flex; align-items: center; font-size: 8px; font-weight: 600; white-space: nowrap; }
  .phone-row .divider { width: 1px; height: 11px; background: var(--white); margin: 0 11px; }
  .phone-row .email { color: var(--sky); font-weight: 500; }
  .social { position: absolute; top: 173px; left: 400px; display: flex; gap: 5px; }
  .social span { width: 19px; height: 19px; border-radius: 50%; background: var(--white); display: block; }
</style>
</head>
<body>
  <header class="hero" role="img" aria-label="Photo of business people joining hands over a meeting table"></header>
  <div class="brand" style="left:68px; top:40px;">HOLVENCREST</div>
  <nav class="site-nav">
    <a style="left:390px">Home</a>
    <a style="left:431px">Approach</a>
    <a style="left:487px">Story</a>
    <a style="left:538px">Blog</a>
    <a class="current" style="left:592px">Contact</a>
  </nav>
  <h1 class="hero-title">Contact Us</h1>
  <p class="hero-lead">Holvencrest is a venture capital studio firm based in Austin TX<br>with a laser focus on raising solid capital for startups</p>

  <main>
    <h2 class="section-title">Build With Us</h2>
    <p class="section-lead">Holvencrest is a venture capital studio firm based in Austin TX with a laser focus on raising solid<br>capital for startups and helping businesses jumpstart their revenue.</p>

    <div class="field line" style="top:468px">Name</div>
    <div class="field line" style="top:511px">Email</div>
    <div class="field line" style="top:554px">Phone</div>
    <div class="field message">Type your message here...</div>
    <div class="submit">Submit Now</div>
  </main>

  <div class="map" role="img" aria-label="Street map of the office neighbourhood"></div>
  <svg class="map-pin" width="36" height="50" viewBox="0 0 36 50" aria-hidden="true">
    <path d="M18 0C8 0 0 8 0 18c0 12 18 32 18 32s18-20 18-32C36 8 28 0 18 0z" fill="#0677ba"/>
    <circle cx="18" cy="17" r="6.5" fill="#ffffff"/>
  </svg>

  <footer class="footer">
    <div class="brand" style="left:81px; top:78px;">HOLVENCREST</div>
    <p class="footer-about">Pellentesque habitant morbi tristique<br>senectus et netus et malesuada fames ac<br>turpis egestas.</p>
    <p class="copyright">© 2022 <span>HOLVENCREST.COM</span></p>

    <h3 class="footer-heading" style="left:289px">Pages</h3>
    <div class="footer-links">
      <a style="top:103px">Home</a>
      <a style="top:119px">Approach</a>
      <a style="top:135px">Story</a>
      <a style="top:151px">Blog</a>
      <a class="current" style="top:167px">Contact</a>
    </div>

    <h3 class="footer-heading" style="left:402px">Contact Details</h3>
    <p class="address">18 Ashcombe Row, Farleigh England</p>
    <div class="phone-row">
      <svg width="13" height="13" viewBox="0 0 24 24" aria-hidden="true" style="margin-right:8px">
        <path d="M6.6 10.8a15.1 15.1 0 006.6 6.6l2.2-2.2a1 1 0 011-.25 11.4 11.4 0 003.6.57 1 1 0 011 1V20a1 1 0 01-1 1A17 17 0 013 4a1 1 0 011-1h3.5a1 1 0 011 1c0 1.25.2 2.45.57 3.6a1 1 0 01-.25 1z" fill="none" stroke="#6fccea" stroke-width="1.6"/>
      </svg>
      <span>+44-7720418365</span>
      <span class="divider"></span>
      <span class="email">hello@holvencrest.com</span>
    </div>
    <div class="social" aria-label="Social links">
      <span></span><span></span><span></span><span></span>
    </div>
  </footer>
</body>
</html>
```